International Trading Company, 'VOLA' needs a Business Card

The company name is "VOLA" and it has own logo design.
I'd like to use its logo on this business card.
I need two side Business Card.
I'll look forward to your great design.
Thank you very much in advance.

Contact Information for Business Card

Company Name : Vola Harbor Limited
Information Example
Tobias Wrenfold
Mobile(use icon please) : 1 (555) 014-2290
Tel(use icon please) : 1 (555) 014-6835
Email(use icon please) : tobias27@volaharbor.example
Address(use icon please) : 482 Larkmoor Rd, New York, NY 10199, USA

```html
<!DOCTYPE html>
<html lang="en">
<head>
<meta charset="utf-8">
<title>Vola Harbor Limited — Business Card</title>
<link href="https://fonts.googleapis.com/css2?family=Roboto:wght@400;500;700&display=swap" rel="stylesheet">
<style>
  :root {
    --page-bg: #e6e6e6;
    --card-front: #050505;
    --card-front-sheen: #1e1e1e;
    --card-back: #ffffff;
    --logo-grey: #5f5f5f;
    --logo-grey-dark: #4a4a4a;
    --text-dark: #4d4d4d;
    --text-body: #555555;
    --url-grey: #5a5a5a;
    --divider: #9a9a9a;
  }
  * { box-sizing: border-box; margin: 0; padding: 0; }
  html, body {
    width: 1200px; height: 1000px; overflow: hidden;
    background: var(--page-bg);
    font-family: "Roboto", Arial, sans-serif;
  }
  .canvas { position: relative; width: 1200px; height: 1000px; }

  .card { position: absolute; left: 220px; width: 760px; box-shadow: 0 6px 18px rgba(0,0,0,0.18); }

  .card-front {
    top: 50px; height: 433px;
    background: linear-gradient(115deg, var(--card-front) 0%, var(--card-front) 58%, var(--card-front-sheen) 66%, #111 85%, #0a0a0a 100%);
  }
  .front-logo {
    position: absolute; left: 0; right: 0; top: 148px;
    text-align: center;
    font-weight: 700; font-size: 124px; line-height: 1; letter-spacing: 4px;
    color: var(--logo-grey);
  }
  .front-url {
    position: absolute; left: 0; right: 0; top: 375px;
    text-align: center; font-size: 16px; color: var(--url-grey); letter-spacing: 0.2px;
  }

  .card-back { top: 524px; height: 436px; background: var(--card-back); }
  .back-logo {
    position: absolute; left: 84px; top: 176px; width: 264px;
    text-align: center;
    font-weight: 700; font-size: 82px; line-height: 1; letter-spacing: 3px;
    color: var(--logo-grey-dark);
  }
  .divider { position: absolute; left: 379px; top: 136px; width: 1px; height: 166px; background: var(--divider); }

  .contact { position: absolute; left: 408px; top: 130px; color: var(--text-body); }
  .contact-name { font-weight: 500; font-size: 19px; letter-spacing: 0.4px; color: var(--text-dark); margin-bottom: 20px; }
  .contact-row { display: flex; align-items: flex-start; font-size: 17px; line-height: 22px; }
  .contact-row + .contact-row { margin-top: 3px; }
  .contact-row.address { margin-bottom: 9px; }
  .contact-icon { width: 13px; height: 13px; margin: 4px 6px 0 0; flex: none; fill: var(--text-body); }
</style>
</head>
<body>
<main class="canvas">
  <section class="card card-front" aria-label="Card front">
    <div class="front-logo">VOLA</div>
    <div class="front-url">www.volaharbor.example</div>
  </section>

  <section class="card card-back" aria-label="Card back">
    <div class="back-logo">VOLA</div>
    <div class="divider"></div>
    <div class="contact">
      <div class="contact-name">TOBIAS WRENFOLD</div>
      <div class="contact-row address">
        <svg class="contact-icon" viewBox="0 0 12 12"><path d="M6 0.5a4 4 0 0 0-4 4c0 3 4 7 4 7s4-4 4-7a4 4 0 0 0-4-4zm0 5.6a1.6 1.6 0 1 1 0-3.2 1.6 1.6 0 0 1 0 3.2z"/></svg>
        <span>482 Larkmoor Rd, New York,<br>NY 10199, USA</span>
      </div>
      <div class="contact-row">
        <svg class="contact-icon" viewBox="0 0 12 12"><path d="M3.5 0.5h5a1 1 0 0 1 1 1v9a1 1 0 0 1-1 1h-5a1 1 0 0 1-1-1v-9a1 1 0 0 1 1-1zm0.3 1.3v7.4h4.4V1.8zM6 9.7a0.6 0.6 0 1 0 0 1.2 0.6 0.6 0 0 0 0-1.2z"/></svg>
        <span>1 (555) 014-2290</span>
      </div>
      <div class="contact-row">
        <svg class="contact-icon" viewBox="0 0 12 12"><path d="M1 3.2C1 2 2 1.5 6 1.5s5 .5 5 1.7v1H8.5V3.4h-5v.8H1zM3 5h6l1.8 2.5V10.5H1.2V7.5zM6 6.2a1.5 1.5 0 1 0 0 3 1.5 1.5 0 0 0 0-3z"/></svg>
        <span>1 (555) 014-6835</span>
      </div>
      <div class="contact-row">
        <svg class="contact-icon" viewBox="0 0 12 12"><path d="M0.5 2.5h11v7h-11zm1 1v.3L6 6.8l4.5-3V3.5zm0 1.5v3.5h9V5L6 8z"/></svg>
        <span>tobias27@volaharbor.example</span>
      </div>
    </div>
  </section>
</main>
</body>
</html>
```